Stationery Set for Brelvo Company

I need to create full stationery design for my company; Business Cards, Envelops, Letter Heads, Calendar.
In the letter head and Envelops... only contact information and website links.
Our company is a Service Management company with different domains of innovative services including Technology Service Management, Education Services, Outsourcing Management, Events Management.
I need a modern and innovative design specially for the business card. I some transparent designs and I like it, but don't limit your innovation to what I mentioned. Sky is limit for your innovation.

Target Market(s)

Middle East & Africa

Industry/Entity Type

Business Management

Colors
34a7d8
0355a3
85acd3
86cae7
cee9f5
cfdeed
e4daeb
f3f1f8
ecf7fb

Requirements
Must have
• Name, Title, Email, Mobile
Nice to have
• We have multiple locations in USA, KSA, EGY, so I need ideas about how to include all contact details maybe QR / Barcode or something else.
• Please see our locations and contact information: www.gofarnix.example
Should not have
• Too much text

```html
<!DOCTYPE html>
<html lang="en">
<head>
<meta charset="utf-8">
<title>Brelvo Company Stationery Set</title>
<link href="https://fonts.googleapis.com/css2?family=Arimo:wght@400;700&family=Exo+2:wght@500&display=swap" rel="stylesheet">
<style>
  :root {
    --bg: #e9eaec;
    --paper: #ffffff;
    --blue-deep: #0355a3;
    --blue-mid: #1f6fd0;
    --blue-sky: #34a7d8;
    --grey-dark: #3a3b3e;
    --grey-mid: #7a7c80;
    --ink: #3c3c3c;
    --ink-soft: #6a6a6a;
  }
  * { margin: 0; padding: 0; box-sizing: border-box; }
  html, body { width: 1200px; height: 937px; overflow: hidden; background: var(--bg); }
  body { position: relative; font-family: "Arimo", Arial, sans-serif; color: var(--ink); }

  .sheet { position: absolute; background: var(--paper); overflow: hidden; }
  .sheet > svg.swoosh { position: absolute; inset: 0; width: 100%; height: 100%; }

  .brand { display: flex; align-items: center; gap: 4px; font-weight: 700; color: var(--blue-mid); white-space: nowrap; }
  .brand-dot { border-radius: 50%; background: var(--blue-mid); flex: none; }

  /* Letterhead */
  .letterhead { left: 185px; top: 66px; width: 386px; height: 547px; }
  .letterhead .brand { position: absolute; left: 17px; top: 31px; font-size: 15px; }
  .letterhead .brand-dot { width: 9px; height: 9px; }
  .contact-block { position: absolute; font-size: 4.6px; line-height: 6.4px; color: var(--ink); }
  .contact-block .strong { font-weight: 700; }
  .contact-line { display: flex; align-items: center; gap: 3px; }
  .contact-line svg { width: 4.5px; height: 4.5px; fill: var(--ink); flex: none; }
  .letterhead .contact-block { left: 303px; top: 25px; }
  .letter-body { position: absolute; left: 35px; top: 140px; width: 296px; font-size: 5.4px; line-height: 7.2px; color: var(--ink); }
  .letter-body p { margin-bottom: 8px; }
  .letter-body .gap-lg { margin-bottom: 22px; }
  .letter-body .strong { font-weight: 700; }
  .signature { width: 26px; height: 16px; background: linear-gradient(90deg, #d9d9d9, #f2f2f2); margin: 2px 0 6px; }

  /* Folder */
  .folder { left: 636px; top: 41px; width: 458px; height: 575px; }
  .folder .brand { position: absolute; left: 95px; top: 274px; font-size: 27px; }
  .folder .brand-dot { width: 14px; height: 14px; }
  .web { position: absolute; font-family: "Exo 2", Arial, sans-serif; font-weight: 500; color: #fff; letter-spacing: 2px; white-space: nowrap; }
  .folder .web { left: 238px; top: 551px; font-size: 11.5px; }

  /* Business cards */
  .card-front { left: 46px; top: 658px; width: 176px; height: 100px; border-radius: 5px; }
  .card-front .brand { position: absolute; left: 9px; top: 14px; font-size: 9.5px; }
  .card-front .brand-dot { width: 6px; height: 6px; }
  .card-front .contact-block { left: 6px; top: 60px; font-size: 3.6px; line-height: 5px; }
  .card-front .contact-line svg { width: 3.6px; height: 3.6px; }
  .card-person { position: absolute; left: 100px; top: 62px; font-size: 4.4px; line-height: 5.6px; }
  .card-person .name { font-weight: 700; letter-spacing: 0.3px; }
  .card-back { left: 46px; top: 785px; width: 176px; height: 100px; border-radius: 5px; }
  .card-back .brand { position: absolute; left: 0; right: 0; top: 42px; justify-content: center; font-size: 11px; }
  .card-back .brand-dot { width: 7px; height: 7px; }

  /* Envelopes */
  .envelope-front { left: 264px; top: 671px; width: 433px; height: 210px; }
  .envelope-front .brand { position: absolute; left: 16px; top: 30px; font-size: 12px; }
  .envelope-front .brand-dot { width: 7px; height: 7px; }
  .envelope-back { left: 737px; top: 671px; width: 431px; height: 210px; }
  .envelope-flap { position: absolute; left: 0; top: 0; width: 100%; height: 72px; border-radius: 0 0 40px 40px;
    background: linear-gradient(90deg, var(--blue-deep) 0%, var(--blue-mid) 40%, #2a7fd8 60%, var(--blue-mid) 80%, var(--blue-deep) 100%); }
  .envelope-back .web { left: 0; right: 0; top: 30px; text-align: center; font-size: 11.5px; }
</style>
</head>
<body>
  <svg width="0" height="0" style="position:absolute">
    <defs>
      <linearGradient id="blue-sweep" x1="0" y1="1" x2="1" y2="0">
        <stop offset="0" stop-color="#0f3f9a"/>
        <stop offset="0.45" stop-color="#1f72d6"/>
        <stop offset="0.7" stop-color="#2b8ae0"/>
        <stop offset="1" stop-color="#0f4fb0"/>
      </linearGradient>
      <linearGradient id="grey-corner" x1="0" y1="0" x2="1" y2="1">
        <stop offset="0" stop-color="#8a8c90"/>
        <stop offset="1" stop-color="#2f3033"/>
      </linearGradient>
      <symbol id="icon-phone" viewBox="0 0 10 10"><path d="M2 1l2 2-1 1.3a6 6 0 0 0 2.7 2.7L7 6l2 2-1.2 1.5C4.5 9.3.7 5.5.5 2.2z"/></symbol>
      <symbol id="icon-mail" viewBox="0 0 10 10"><path d="M0 2h10v6H0zM.8 2.6 5 5.6l4.2-3z" fill-rule="evenodd"/></symbol>
      <symbol id="icon-globe" viewBox="0 0 10 10"><path d="M5 0a5 5 0 1 0 0 10A5 5 0 0 0 5 0zm0 1.2a3.8 3.8 0 1 1 0 7.6 3.8 3.8 0 0 1 0-7.6z"/></symbol>
    </defs>
  </svg>

  <!-- Letterhead -->
  <section class="sheet letterhead">
    <svg class="swoosh" viewBox="0 0 386 547" preserveAspectRatio="none" aria-hidden="true">
      <path d="M386 445 L386 547 L355 547 C372 520 382 490 386 445Z" fill="url(#grey-corner)"/>
      <path d="M300 547 C345 520 375 470 386 390 L386 430 C380 495 362 530 343 547Z" fill="url(#blue-sweep)"/>
    </svg>
    <div class="brand"><span class="brand-dot"></span>Brelvo Company</div>
    <div class="contact-block">
      <div class="strong">Office 2204, Tower Hall</div>
      <div class="strong">Coastline Road, Unit 8</div>
      <div class="contact-line"><svg><use href="#icon-phone"/></svg>+00 555 0184</div>
      <div class="contact-line"><svg><use href="#icon-mail"/></svg>mail@gofarnix.example</div>
      <div class="contact-line"><svg><use href="#icon-globe"/></svg>www.gofarnix.example</div>
    </div>
    <div class="letter-body">
      <p>July 2, 2012</p>
      <p><span class="strong">Dear Sir,</span><br>ABC Building, def St., Country Name</p>
      <p>Our team delivers service management across technology, education, outsourcing and events. We plan each project with care, keep clients informed at every step and measure results against clear goals. This letter confirms the terms we discussed and the schedule agreed for the coming quarter, with our offices ready to support you in each region.</p>
      <p class="gap-lg">Please review the attached summary and share any questions with our coordinator before the start date.</p>
      <p>We value the trust you place in our work and look forward to building a lasting partnership. Our staff in each location will follow up with the details you need, including contacts, timelines and the reports promised at our last meeting, so that every stage runs smoothly and on time.</p>
      <p>Best Regards,</p>
      <div class="signature" role="img" aria-label="Handwritten signature"></div>
      <p><span class="strong">Dana Morel</span><br>Director<br><br>ABC Building, def St., Country Name</p>
    </div>
  </section>

  <!-- Presentation folder -->
  <section class="sheet folder">
    <svg class="swoosh" viewBox="0 0 458 575" preserveAspectRatio="none" aria-hidden="true">
      <path d="M290 0 L458 0 L458 235 C440 130 385 45 290 0Z" fill="url(#grey-corner)"/>
      <path d="M145 575 C345 470 440 290 335 45 C405 95 445 170 458 255 L458 575Z" fill="url(#blue-sweep)"/>
    </svg>
    <div class="brand"><span class="brand-dot"></span>Brelvo Company</div>
    <div class="web">www.gofarnix.example</div>
  </section>

  <!-- Business card, front -->
  <section class="sheet card-front">
    <svg class="swoosh" viewBox="0 0 176 100" preserveAspectRatio="none" aria-hidden="true">
      <path d="M140 0 L176 0 L176 45 C170 25 158 10 140 0Z" fill="url(#grey-corner)"/>
      <path d="M120 100 C160 85 178 50 155 8 C168 20 174 35 176 50 L176 100Z" fill="url(#blue-sweep)"/>
    </svg>
    <div class="brand"><span class="brand-dot"></span>Brelvo Company</div>
    <div class="contact-block">
      <div class="strong">Office 2204, Tower Hall</div>
      <div class="strong">Coastline Road, Unit 8</div>
      <div class="contact-line"><svg><use href="#icon-phone"/></svg>+00 555 0184</div>
      <div class="contact-line"><svg><use href="#icon-mail"/></svg>mail@gofarnix.example</div>
      <div class="contact-line"><svg><use href="#icon-globe"/></svg>www.gofarnix.example</div>
    </div>
    <div class="card-person">
      <div class="name">SAMI IDRIS</div>
      <div>Managing Director</div>
    </div>
  </section>

  <!-- Business card, back -->
  <section class="sheet card-back">
    <div class="brand"><span class="brand-dot"></span>Brelvo Company</div>
  </section>

  <!-- Envelope, front -->
  <section class="sheet envelope-front">
    <svg class="swoosh" viewBox="0 0 433 210" preserveAspectRatio="none" aria-hidden="true">
      <path d="M330 0 L433 0 L433 70 C410 35 375 12 330 0Z" fill="url(#grey-corner)"/>
      <path d="M250 210 C350 185 420 130 380 15 C410 35 428 60 433 85 L433 210Z" fill="url(#blue-sweep)"/>
    </svg>
    <div class="brand"><span class="brand-dot"></span>Brelvo Company</div>
  </section>

  <!-- Envelope, back -->
  <section class="sheet envelope-back">
    <div class="envelope-flap"></div>
    <div class="web">www.gofarnix.example</div>
  </section>
</body>
</html>
```